Car Club Website- Kestrel Roadster Club of New Zealand

We have been running a website in NZ for Kestrel Roadster Car enthusiasts. The design was fairly basic and is in serious need of a revamp, http://garagepalisade.example.org/index.html. We are looking for a dynamic design that will be visually attractive ( and obvious ) to our visitors and incorporates the fundamentals of the previous website. The inmportant tabs are the forum, gallery and events and the website needs to be easy to use for everyone.

This is all about the cars and the people. Visually, you need to recognise that we are a NZ Car Club and as such we do not want graphics of Left Hand Drive Cars or anything obviously NOT from NZ.
Thanks, cheers Wes

I AM VERY INTERESTED TO SEE SOMETHING THAT IS TOTALLY DIFFERENT TO ANYTHING YET POSTED. THE DESIGNS WE HAVE ARE GOOD AND I WILL PICK ONE OF THOSE BUT REALLY WANT TO SEE SOMETHING CREATIVE AND EYE CATCHING. I HAVE NOW CHANGED TO NON REFUNDABLE SO SOMEONE WILL GET PAID.
Updates

HI All, thanks for input so far but I have not seen a really creative left field approach yet which I am looking for. Thanks, cheers Wes

Target Market(s)

Car Enthusiasts

Industry/Entity Type

Events

Requirements
Must have
• as per link website
Should not have
• Any obvious graphics not from NZ

```html
<!DOCTYPE html>
<html lang="en">
<head>
<meta charset="utf-8">
<title>Kestrel Roadster Club of New Zealand</title>
<link rel="stylesheet" href="https://fonts.googleapis.com/css2?family=Questrial&family=Open+Sans:wght@400;600;700&display=swap">
<style>
:root{
  --ink:#222;
  --panel:#333;
  --panel-dark:#1c1c1c;
  --black:#000;
  --white:#fff;
  --rule:#222;
  --muted:#b5b5b5;
  --page:#fff;
}
*{box-sizing:border-box;margin:0;padding:0}
html,body{width:993px;height:1200px;overflow:hidden;background:var(--page)}
body{position:relative;font-family:"Open Sans",sans-serif;color:var(--ink)}
.abs{position:absolute}
.brand{left:101px;top:22px;font-family:"Questrial",sans-serif;color:#2b2b2b;line-height:1}
.brand .name{font-size:38px;display:block}
.brand .region{font-size:30px;display:block;margin-top:6px}
.social{left:770px;top:21px;display:flex;gap:13px}
.social span{width:27px;height:27px;border-radius:50%;background:var(--muted)}
.top-nav{left:700px;top:102px;display:flex;gap:17px;font-family:"Questrial",sans-serif;font-size:12.5px;letter-spacing:.3px}
.hero-photo{left:102px;top:123px;width:512px;height:263px;background:linear-gradient(180deg,#cfc6bb 0%,#b9a893 40%,#6a6866 70%,#8d8a86 100%)}
.hero-panel{left:614px;top:123px;width:264px;height:263px;background:var(--panel);color:var(--white)}
.hero-panel h2{position:absolute;left:12px;top:62px;font-family:"Questrial",sans-serif;font-weight:400;font-size:23px}
.hero-panel p{position:absolute;left:17px;top:103px;width:250px;font-size:12.6px;line-height:15px}
.btn{display:flex;height:30px;font-weight:600;font-size:13px}
.btn .label{flex:1;display:flex;align-items:center;justify-content:center}
.btn .arrow{width:37px;display:flex;align-items:center;justify-content:center;font-size:16px;font-weight:700}
.btn.light .label{background:var(--white);color:var(--ink)}
.btn.light .arrow{background:var(--black);color:var(--white)}
.btn.dark .label{background:var(--panel);color:var(--white)}
.btn.dark .arrow{background:var(--black);color:var(--white)}
.hero-panel .btn{position:absolute;left:20px;top:182px;width:135px}
.dots{left:457px;top:394px;display:flex;gap:6px}
.dots span{width:11px;height:11px;border-radius:50%;background:var(--panel)}
.dots span:first-child{background:var(--white);border:2px solid #555}
.side{left:102px;top:426px;width:182px;height:361px;box-shadow:0 1px 3px rgba(0,0,0,.4)}
.side-menu{height:172px;background:linear-gradient(180deg,#3d3d3d,#2e2e2e);padding-top:12px}
.side-menu a{display:flex;align-items:center;height:30px;color:var(--white);text-decoration:none;font-family:"Questrial",sans-serif;font-size:17px}
.side-menu a::before{content:"";width:26px;height:1px;background:var(--white);margin-right:11px;margin-left:-2px}
.side-cal{height:159px;background:var(--panel-dark);color:var(--white);padding-top:9px}
.side-cal h3{display:flex;align-items:center;font-family:"Questrial",sans-serif;font-weight:400;font-size:24px;letter-spacing:.5px}
.side-cal h3::before{content:"";width:20px;height:2px;background:var(--white);margin:0 8px 0 0}
.side-cal li{list-style:none;font-size:10.5px;height:26px;display:flex;align-items:center;padding-left:3px}
.side-cal li b{font-weight:400;width:40px}
.side .btn{height:30px}
.main{left:300px;top:424px;width:451px}
.main h1{display:flex;align-items:center;font-family:"Questrial",sans-serif;font-weight:400;font-size:22px;color:#333}
.main h1::after{content:"";flex:1;height:1px;background:var(--rule);margin-left:7px}
.main p{font-size:10.2px;line-height:12.4px;margin-top:9px;color:#222}
.main .rule{height:1px;background:var(--rule);margin:22px 0 0 4px}
.main .second{margin-top:21px}
.main-btn{left:611px;top:737px;width:135px}
.divider{left:756px;top:429px;width:1px;height:303px;background:var(--rule)}
.ads{left:766px;top:424px;width:115px;text-align:center;font-family:"Questrial",sans-serif;font-size:22px;line-height:22px;color:#222}
.ad-slot{left:773px;top:486px;width:97px;height:230px}
.ad-note{left:764px;top:734px;width:115px;font-size:7.5px;line-height:10px;color:#333;text-transform:uppercase}
.card{top:807px;width:248px;height:308px;box-shadow:0 1px 3px rgba(0,0,0,.35)}
.card .photo{height:149px}
.card .body{height:131px;background:var(--black);color:var(--white);padding:10px 20px 0}
.card h4{font-family:"Questrial",sans-serif;font-weight:400;font-size:17.5px;margin-bottom:10px}
.card p{font-size:10.3px;line-height:12.4px}
.card .btn{height:29px}
.footer{left:0;top:1151px;width:993px;height:49px;background:var(--panel);display:flex;justify-content:center;align-items:center;gap:0;color:var(--white);font-family:"Questrial",sans-serif;font-size:12px}
.footer a{color:var(--white);text-decoration:none;margin:0 10px}
</style>
</head>
<body>

<div class="abs brand"><span class="name">Kestrel Roadster Club</span><span class="region">of new Zealand</span></div>
<div class="abs social" aria-label="Social links"><span></span><span></span><span></span></div>
<nav class="abs top-nav"><span>FORUM</span><span>GALLERY</span><span>EVENTS</span></nav>

<div class="abs hero-photo" role="img" aria-label="Blue roadster with white stripes on a desert road"></div>
<div class="abs hero-panel">
  <h2>Kestrel Club</h2>
  <p>Welcome to Kestrel Roadster Club of New Zealand. We love Kestrel's style At home On the Track or On Show. Share your interest about Kestrel's now and join our Club</p>
  <div class="btn light"><span class="label">Learn More</span><span class="arrow">&gt;</span></div>
</div>
<div class="abs dots"><span></span><span></span><span></span><span></span></div>

<aside class="abs side">
  <nav class="side-menu">
    <a>Home</a><a>Calendar</a><a>Membership</a><a>Advertisers</a><a>Contact Us</a>
  </nav>
  <div class="side-cal">
    <h3>CALENDAR</h3>
    <ul>
      <li><b>15/12</b>Lorem Ipsum is simply...</li>
      <li><b>17/12</b>&nbsp;dummy text...</li>
      <li><b>19/12</b>Lorem Ipsum is simply...</li>
      <li><b>25/12</b>&nbsp;dummy text...</li>
    </ul>
  </div>
  <div class="btn light"><span class="label">Learn More</span><span class="arrow">&gt;</span></div>
</aside>

<main class="abs main">
  <h1>Welcome to Kestrel Club</h1>
  <p>This is not an official website related to the manufacture of Kestrel Roadster cars but it is a website devoted to all those that share a passion for the Kestrel Roadster.<br>
  Welcome to our website. Our aim is to make this site user friendly and we have included a 'Forum' for the benefit of all Kestrel Roadster owners in New Zealand regardless of Kestrel kit type. Our intent for the Forum is to give those people interested/active in the Kestrel Roadster NZ scene a common vehicle to share ideas, problem solve and plan events. Our Calendar lists up-to-date and upcoming events. Check this regularly, especially for those last-minute runs that are often organised at very short notice upon the discovery of fine weather in Auckland!</p>
  <div class="rule"></div>
  <p class="second">No matter where your taste lies, the Kestrel Roadster Club of New Zealand has members that fit all categories.<br>
  From showing your prize possession off at a local car show or promotional event, to risking it all on the race track. &nbsp;If you're into Kestrel's then this is the place to be!<br>
  The club regularly attends shows such as the Harbourside Concours at Riverbank, All Marques Day and fundraising events such as the Charity Cruise Runs. &nbsp;Just for that adrenalin rush a few hot laps at Ridgeline Raceway or even Coastal Rally, to test your nerves!<br>
  So if you're into Kestrel's, thinking of building one, looking for advice, or just need to be near one check out the Calendar pages or contact details</p>
</main>
<div class="abs btn dark main-btn"><span class="label">Learn More</span><span class="arrow">&gt;</span></div>

<div class="abs divider"></div>
<div class="abs ads">Advertising<br>Banners</div>
<svg class="abs ad-slot" viewBox="0 0 97 230" aria-label="Advertising banner space">
  <rect x=".5" y=".5" width="96" height="229" fill="none" stroke="#222"/>
  <line x1="0" y1="0" x2="97" y2="230" stroke="#222"/>
  <line x1="97" y1="0" x2="0" y2="230" stroke="#222"/>
</svg>
<p class="abs ad-note">Please support our advertisers who fund this site for the benefit of all</p>

<article class="abs card" style="left:102px">
  <div class="photo" role="img" aria-label="Black roadster parked in front of a house" style="background:linear-gradient(180deg,#8a8a6a,#5d6350 45%,#1d1f22 75%,#777 100%)"></div>
  <div class="body"><h4>Fest no1</h4><p>Lorem Ipsum is simply dummy text of the printing and typesetting industry. Lorem Ipsum has been the industry's standard dummy text ever since the 1500s, when an unknown printer took a galley of type and scrambled.</p></div>
  <div class="btn light"><span class="label">Learn More</span><span class="arrow">&gt;</span></div>
</article>
<article class="abs card" style="left:367px">
  <div class="photo" role="img" aria-label="Blue roadster at an outdoor car show" style="background:linear-gradient(180deg,#b8aa9a,#2a2f8a 40%,#16185a 80%,#4a4a4a 100%)"></div>
  <div class="body"><h4>Fest no1</h4><p>Lorem Ipsum is simply dummy text of the printing and typesetting industry. Lorem Ipsum has been the industry's standard dummy text ever since the 1500s, when an unknown printer took a galley of type and scrambled.</p></div>
  <div class="btn light"><span class="label">Learn More</span><span class="arrow">&gt;</span></div>
</article>
<article class="abs card" style="left:631px">
  <div class="photo" role="img" aria-label="Row of silver and red roadsters lined up at a meet" style="background:linear-gradient(100deg,#9aa5b0,#b7c0c8 45%,#c8302e 75%,#d33 100%)"></div>
  <div class="body"><h4>Fest no3</h4><p>Lorem Ipsum is simply dummy text of the printing and typesetting industry. Lorem Ipsum has been the industry's standard dummy text ever since the 1500s, when an unknown printer took a galley of type and scrambled.</p></div>
  <div class="btn light"><span class="label">Learn More</span><span class="arrow">&gt;</span></div>
</article>

<footer class="abs footer">
  <a>HOME</a><a>CALENDAR</a><a>MEMBERSHIP</a><a>ADVERTISERS</a><a>CONTACT US</a><a>FORUM</a><a>GALLERY</a><a>EVENTS</a>
</footer>

</body>
</html>
```